Website for criminal defense attorney

Need a website that informs reader of my 26 years of practice, wins, practice areas (federal and capital cases, serious felonies, custody battles, etc), allows for payments (coinlet, quidora, zuvix, brisk, cards), etc. Client have referred to me as "The Iron Warden" "The Verdict" "Centurion". I do tend to use The Iron Warden motto and always play to win. Based in Atlanta but travel to other states. Color preferences are black and old gold, masonic themes and images (hidden), Kappa Rho Tau fraternity themes or images (likewise subtle or hidden), Spartan and warrior themes. Want strong, but not arrogant, Not about my ego, but about my ability to deliver. Have included business card, but not married to it and want to begin a brand of high end representation for remainder of my career.

```html
<!DOCTYPE html>
<html lang="en">
<head>
<meta charset="utf-8">
<title>Marcus T. Bellamy, LLC — Attorney at Law</title>
<link href="https://fonts.googleapis.com/css2?family=Crimson+Pro:wght@400;500&family=Open+Sans:wght@400;600&display=swap" rel="stylesheet">
<style>
:root{
  --canvas:#efe5c2;
  --gold:#cdb43a;
  --gold-deep:#b89f2a;
  --ink:#1b1b1b;
  --muted:#6d6d6d;
  --white:#ffffff;
  --soft:#f3f3f3;
  --night:#161616;
  --night-2:#1f1f1f;
  --night-3:#2a2a2a;
  --serif:"Crimson Pro", Georgia, serif;
  --sans:"Open Sans", Arial, sans-serif;
}
*{box-sizing:border-box;margin:0;padding:0}
html,body{width:1200px;height:2294px;overflow:hidden;background:var(--canvas)}
body{position:relative;font-family:var(--sans);color:var(--ink)}

.showcase-title{position:absolute;top:62px;left:0;width:1200px;text-align:center;font-family:var(--serif);font-weight:400;font-size:54px;letter-spacing:1px;color:var(--ink)}
.showcase-sub{position:absolute;top:128px;left:0;width:1200px;display:flex;align-items:center;justify-content:center;gap:12px;font-family:var(--serif);font-size:35px;color:var(--ink)}
.showcase-sub::before,.showcase-sub::after{content:"";width:148px;height:1px;background:#555}

.site{position:absolute;width:494px;overflow:hidden;box-shadow:0 2px 10px rgba(0,0,0,.12)}
.site.light{left:72px;top:257px;--page:var(--white);--alt:var(--soft);--text:var(--ink);--body:var(--muted);--card:var(--white)}
.site.dark{left:634px;top:250px;--page:#141414;--alt:var(--night);--text:#f2f2f2;--body:#c9c9c9;--card:var(--night-2)}
.site section,.site header,.site footer{position:relative;width:494px}

.site-header{height:45px;background:var(--page);color:var(--text)}
.topline{position:absolute;top:4px;left:46px;font-family:var(--serif);font-size:5.5px;line-height:7px}
.topline b{color:var(--gold);font-weight:400}
.util{position:absolute;top:5px;right:46px;display:flex;align-items:center;gap:3px}
.util .dot{width:5px;height:5px;border-radius:50%;background:var(--gold)}
.util .chip{width:9px;height:5px;background:#9aa4b8;border-radius:1px}
.util .sep{width:1px;height:5px;background:#bbb}
.rule{position:absolute;top:14px;left:46px;right:46px;height:1px;background:var(--gold);opacity:.5}
.brand{position:absolute;top:5px;left:50%;transform:translateX(-50%);background:var(--page);padding:0 6px;text-align:center;font-family:var(--serif);color:var(--gold)}
.brand .mark{display:block;width:14px;height:18px;margin:0 auto 3px;border:1px solid var(--gold)}
.brand .name{display:block;font-size:5px;letter-spacing:.3px;white-space:nowrap}
.nav{position:absolute;top:28px;display:flex;gap:11px;font-family:var(--serif);font-size:6px}
.nav.left{left:84px}.nav.right{left:313px}

.hero{height:245px;background:linear-gradient(180deg,#3b3e43 0%,#2a2d31 55%,#1d1f22 100%);color:#fff;text-align:center}
.hero-photo{position:absolute;inset:0}
.hero-inner{position:absolute;top:60px;left:0;width:494px}
.hero h2{font-family:var(--serif);font-weight:400;font-size:19px;letter-spacing:.5px}
.hero .tag{font-family:var(--serif);font-size:13.5px;margin-top:2px;display:flex;align-items:center;justify-content:center;gap:6px}
.hero .tag::before,.hero .tag::after{content:"";width:54px;height:1px;background:rgba(255,255,255,.5)}
.hero p{font-size:6.5px;line-height:12px;margin:6px auto 0;width:150px}
.btn{display:inline-block;background:var(--gold);color:#fff;font-size:6px;font-weight:600;letter-spacing:.5px;padding:6px 13px}
.btn.ink{background:var(--ink)}
.hero .btn{margin-top:10px}
.pager{font-family:var(--serif);font-size:7px;display:flex;justify-content:center;gap:8px;margin-top:10px}
.slant{position:absolute;left:0;bottom:0;display:block}

.label{font-size:8px;color:var(--gold);display:flex;align-items:center;justify-content:center;gap:5px;letter-spacing:.5px}
.label::before,.label::after{content:"";width:25px;height:1px;background:var(--gold)}
.sec-title{font-family:var(--serif);font-weight:400;font-size:14px;letter-spacing:1px;text-align:center;margin-top:2px;color:var(--text)}

.about{height:276px;background:var(--page)}
.about .head{position:absolute;top:36px;width:494px}
.about-copy{position:absolute;top:96px;left:46px;width:200px;color:var(--text)}
.about-copy h3{font-family:var(--serif);font-weight:400;font-size:12px;letter-spacing:.5px}
.about-copy p{font-size:6.4px;line-height:12.4px;color:var(--body);margin-top:8px}
.about-copy .btn{margin-top:12px}
.frame{position:absolute;left:291px;top:92px;width:157px;height:149px;background:var(--gold)}
.frame .pager{position:absolute;bottom:4px;left:32px;margin:0;color:#fff;font-size:6.5px}
.video{position:absolute;left:282px;top:96px;width:157px;height:119px;background:linear-gradient(135deg,#d8dde2,#8a8f94 55%,#3d4248)}
.play{position:absolute;left:70px;top:52px;width:16px;height:16px;border-radius:50%;background:var(--gold)}
.play::after{content:"";position:absolute;left:6px;top:4.5px;border-left:5px solid #fff;border-top:3.5px solid transparent;border-bottom:3.5px solid transparent}

.practice{height:289px;background:var(--gold)}
.practice h2,.awards h2,.case h2{position:absolute;top:30px;width:494px;text-align:center;font-family:var(--serif);font-weight:400;font-size:14px;letter-spacing:1px;color:#fff}
.practice h2::after,.awards h2::after{content:"";display:block;width:46px;height:1px;background:#fff;margin:6px auto 0}
.tiles{position:absolute;left:55px;top:82px;display:grid;grid-template-columns:repeat(3,120px);grid-auto-rows:77px;gap:9px 12px}
.tile{position:relative;border:2px solid #fff;background:linear-gradient(160deg,#6f7275,#2b2d30);display:flex;align-items:flex-end;justify-content:center;padding-bottom:10px;font-family:var(--serif);font-size:6.4px;color:#fff;text-transform:uppercase}
.tile.b{background:linear-gradient(160deg,#3a3a3a,#151515)}
.tile.c{background:linear-gradient(160deg,#8a6e5a,#3a3634)}

.reviews{height:240px;background:var(--alt)}
.reviews .head{position:absolute;top:30px;width:494px}
.quote{position:absolute;top:83px;width:196px;padding-left:20px}
.quote::before{content:"\201C";position:absolute;left:0;top:-8px;font-family:var(--serif);font-size:24px;color:var(--gold);line-height:1}
.quote p{font-size:6.4px;line-height:12.4px;color:var(--body)}
.quote .by{font-family:var(--serif);font-size:6px;color:var(--gold);margin-top:8px}
.quote .by span{opacity:.8}
.reviews .pager{position:absolute;top:171px;width:494px;margin:0;color:var(--text)}
.center-btn{position:absolute;width:494px;text-align:center}

.awards{height:205px;background:var(--gold)}
.badges{position:absolute;left:49px;top:74px;display:grid;grid-template-columns:repeat(4,94px);gap:7px}
.badge{height:96px;background:#fff;border:2px solid #fff;outline:1px solid rgba(255,255,255,.7);outline-offset:2px;display:flex;align-items:center;justify-content:center}
.badge .seal{width:40px;height:40px;border-radius:50%;border:3px solid var(--gold);background:#22306b}

.blog{height:282px;background:var(--page)}
.blog .head{position:absolute;top:42px;width:494px}
.post{position:absolute;top:93px;width:175px;height:107px;background:var(--card);box-shadow:0 2px 8px rgba(0,0,0,.1);padding:12px 12px 0 31px}
.post::before{content:"";position:absolute;left:12px;top:0;width:8px;height:38px;background:var(--gold)}
.post h4{font-size:7.6px;font-weight:600;line-height:12px;color:var(--text)}
.post p{font-size:6px;line-height:12px;color:var(--body);margin-top:5px}
.post .more{font-family:var(--serif);font-size:6.5px;color:var(--gold);letter-spacing:.8px;margin-top:6px}

.case{height:178px;background:var(--gold)}
.form{position:absolute;left:121px;top:68px;width:254px}
.row{display:grid;grid-template-columns:repeat(3,1fr);gap:4px}
.field{height:18px;background:#fff;font-size:5.5px;color:#999;padding:6px 8px}
.field.msg{height:28px;margin-top:4px}
.case .center-btn{top:127px}

.site-footer{height:203px;background:linear-gradient(90deg,#1c1c1c 55%,#161616 55%);color:#ddd}
.foot-brand{position:absolute;top:20px;left:46px;font-family:var(--serif)}
.foot-brand .mark{width:22px;height:22px;border:1.5px solid #fff;margin-left:22px}
.foot-brand .name{font-size:6.5px;margin-top:6px;letter-spacing:.3px}
.contact{position:absolute;top:70px;left:46px;font-size:6px;line-height:12px}
.contact li{list-style:none;display:flex;gap:8px;margin-bottom:6px}
.contact svg{flex:none;margin-top:2px}
.foot-col{position:absolute;top:55px;font-size:6px;line-height:12.4px}
.foot-col h5{font-size:6.5px;font-weight:600;margin-bottom:8px}
.foot-col.nav-col{left:183px}
.foot-col.news-col{left:298px;width:100px}
.input{height:18px;background:#fff;color:#777;font-size:5.5px;padding:5px 7px;margin-top:7px;width:92px}
.foot-col .btn{width:92px;text-align:center;margin-top:6px;padding:5px 0}
.foot-rule{position:absolute;top:170px;left:46px;right:46px;height:1px;background:#333}
.copy{position:absolute;top:183px;left:46px;font-size:6px}
.social{position:absolute;top:180px;left:298px;display:flex;gap:5px}
.social i{width:13px;height:13px;border-radius:50%;background:var(--gold)}
.social i+i{background:transparent;border:1px solid #fff}
</style>
</head>
<body>

<h1 class="showcase-title">MARCUS T. BELLAMY, LLC</h1>
<div class="showcase-sub">Attorney at Law</div>

<div class="site light">
  <header class="site-header">
    <div class="rule"></div>
    <div class="topline">Call a firm you can count on <b>404-555-0172</b></div>
    <div class="util"><svg width="6" height="6" viewBox="0 0 10 10"><circle cx="4" cy="4" r="3" fill="none" stroke="#cdb43a" stroke-width="1.4"/><path d="M6.5 6.5L9 9" stroke="#cdb43a" stroke-width="1.4"/></svg><span class="sep"></span><span class="dot" aria-label="Social profile"></span><span class="dot" aria-label="Social profile"></span><span class="sep"></span><span class="chip"></span><span class="chip"></span><span class="chip"></span><span class="chip"></span></div>
    <div class="brand"><span class="mark"></span><span class="name">MARCUS T. BELLAMY, LLC</span></div>
    <nav class="nav left"><span>Home</span><span>Practice Area</span><span>About Us</span></nav>
    <nav class="nav right"><span>News</span><span>Testimonials</span><span>Contact</span></nav>
  </header>

  <section class="hero">
    <div class="hero-photo" role="img" aria-label="Dusk photograph of a city skyline"></div>
    <div class="hero-inner">
      <h2>MARCUS T. BELLAMY, LLC</h2>
      <div class="tag">Attorney at Law</div>
      <p>Sed ut perspiciatis unde omnis iste natus error sit voluptatem accusantium.</p>
      <span class="btn">GET A QUOTE</span>
      <div class="pager"><span>←</span><span>1 of 3</span><span>→</span></div>
    </div>
    <svg class="slant" width="494" height="20"><polygon points="0,20 494,0 494,20" fill="#cdb43a"/></svg>
  </section>

  <section class="about">
    <div class="head"><div class="label">ABOUT</div><div class="sec-title">MARCUS T. BELLAMY</div></div>
    <div class="about-copy">
      <h3>26 YEARS OF PRACTICE</h3>
      <p>Sed ut perspiciatis unde omnis iste natus error sit voluptatem accus antium dolore mque laudantium, totam rem aperiam, eaque ipsa quae ab illo inventore veritatis et quasi architecto beatae vitae dicta sunt explicabo. Nemo enim ipsam voltatem quia voluptas sit aspernatur aut odit aut fugit.</p>
      <span class="btn">LEARN MORE</span>
    </div>
    <div class="frame"><div class="pager"><span>←</span><span>1 of 3</span><span>→</span></div></div>
    <div class="video" role="img" aria-label="Video still of the attorney in conversation with a client at a desk"><span class="play"></span></div>
  </section>

  <section class="practice">
    <h2>PRACTICE AREAS</h2>
    <div class="tiles">
      <div class="tile" role="img" aria-label="Courthouse columns">Federal and Capital Cases</div>
      <div class="tile b" role="img" aria-label="Dim interior scene">Serious Felonies</div>
      <div class="tile c" role="img" aria-label="Family meeting with a counselor">Custody Battles</div>
      <div class="tile" role="img" aria-label="Laptop at a legal office">Lorem Ipsum</div>
      <div class="tile c" role="img" aria-label="Signing documents">Lorem Ipsum</div>
      <div class="tile" role="img" aria-label="Colleagues reviewing papers">Lorem Ipsum</div>
    </div>
    <svg class="slant" width="494" height="20"><polygon points="0,2 494,14 494,20 0,20" fill="#161616"/></svg>
  </section>

  <section class="reviews">
    <div class="head"><div class="label">REVIEWS</div><div class="sec-title">OUR CLIENTS</div></div>
    <div class="quote" style="left:46px"><p>At vero eos et accusamus et iusto odio dignissimos ducimus qui blanditiis prae entium volupt deleniti atque corrupti quos cati cupiditate non provident, sique sunt in culpa qui officia.</p><div class="by">JULIAN <span>/ Oct 25 2021</span></div></div>
    <div class="quote" style="left:261px"><p>At vero eos et accusamus et iusto odio dignissimos ducimus qui blanditiis prae entium volupt deleniti atque corrupti quos cati cupiditate non provident, sique sunt in culpa qui officia.</p><div class="by">JULIAN <span>/ Oct 25 2021</span></div></div>
    <div class="pager"><span>←</span><span>1 of 3</span><span>→</span></div>
    <div class="center-btn" style="top:193px"><span class="btn">VIEW ALL</span></div>
  </section>

  <section class="awards">
    <h2>AWARDS AND MEMBERSHIP</h2>
    <div class="badges">
      <div class="badge" role="img" aria-label="Membership badge"><span class="seal"></span></div>
      <div class="badge" role="img" aria-label="Membership badge"><span class="seal"></span></div>
      <div class="badge" role="img" aria-label="Membership badge"><span class="seal"></span></div>
      <div class="badge" role="img" aria-label="Membership badge"><span class="seal"></span></div>
    </div>
  </section>

  <section class="blog">
    <svg class="slant" style="top:0;bottom:auto" width="494" height="20"><polygon points="0,0 494,0 494,18 0,6" fill="#161616"/></svg>
    <div class="head"><div class="label">NEWS</div><div class="sec-title">LATEST BLOG</div></div>
    <article class="post" style="left:61px"><h4>Sed ut perspiciatis unde omnis natus error sit volupt</h4><p>Sed ut perspiciatis unde omnis natus error sit volupt Sed ut perspiciati unde omnis natus error.</p><div class="more">READ MORE &nbsp;→</div></article>
    <article class="post" style="left:258px"><h4>Sed ut perspiciatis unde omnis natus error sit volupt</h4><p>Sed ut perspiciatis unde omnis natus error sit volupt Sed ut perspiciati unde omnis natus error.</p><div class="more">READ MORE &nbsp;→</div></article>
    <div class="center-btn" style="top:238px"><span class="btn">VIEW ALL</span></div>
  </section>

  <section class="case">
    <h2>GET YOUR CASE STARTED</h2>
    <div class="form">
      <div class="row"><div class="field">Name</div><div class="field">Email</div><div class="field">Phone</div></div>
      <div class="field msg">Message</div>
    </div>
    <div class="center-btn"><span class="btn ink">SUBMIT NOW</span></div>
  </section>

  <footer class="site-footer">
    <div class="foot-brand"><div class="mark"></div><div class="name">MARCUS T. BELLAMY, LLC</div></div>
    <ul class="contact">
      <li><svg width="7" height="9" viewBox="0 0 10 13"><path d="M5 0a5 5 0 0 1 5 5c0 3.5-5 8-5 8S0 8.5 0 5a5 5 0 0 1 5-5z" fill="#cdb43a"/><circle cx="5" cy="5" r="2" fill="#1c1c1c"/></svg><span>2400 Harbor Crest Avenue<br>suite 300, Ridgeport,<br>Ohio 44102</span></li>
      <li><svg width="7" height="7" viewBox="0 0 10 10"><path d="M2 0l2 2.5-1.2 1.3a6 6 0 0 0 3.4 3.4L7.5 6 10 8l-1.5 2C4 10 0 6 0 1.5z" fill="#cdb43a"/></svg><span>404-555-0172</span></li>
      <li><svg width="8" height="6" viewBox="0 0 10 7"><rect width="10" height="7" fill="#cdb43a"/><path d="M0 0l5 4 5-4" fill="none" stroke="#1c1c1c"/></svg><span>attorneybellamy@<br>mailhub.com</span></li>
    </ul>
    <div class="foot-col nav-col"><h5>Navigation</h5>Home<br>Practice Area<br>About Us<br>News<br>Testimonials<br>Contact</div>
    <div class="foot-col news-col"><h5>Newsletter</h5>At vero eos et accusamus et iusto odio dignissimos ducimus qui<div class="input">Enter email</div><span class="btn">SUBMIT NOW</span></div>
    <div class="foot-rule"></div>
    <div class="copy">2021 Marcus T. Bellamy. All Rights Reserved.</div>
    <div class="social" aria-label="Social profiles"><i></i><i></i></div>
  </footer>
</div>

<div class="site dark">
  <header class="site-header">
    <div class="rule"></div>
    <div class="topline">Call a firm you can count on <b>404-555-0172</b></div>
    <div class="util"><svg width="6" height="6" viewBox="0 0 10 10"><circle cx="4" cy="4" r="3" fill="none" stroke="#cdb43a" stroke-width="1.4"/><path d="M6.5 6.5L9 9" stroke="#cdb43a" stroke-width="1.4"/></svg><span class="sep"></span><span class="dot" aria-label="Social profile"></span><span class="dot" aria-label="Social profile"></span><span class="sep"></span><span class="chip"></span><span class="chip"></span><span class="chip"></span><span class="chip"></span></div>
    <div class="brand"><span class="mark"></span><span class="name">MARCUS T. BELLAMY, LLC</span></div>
    <nav class="nav left"><span>Home</span><span>Practice Area</span><span>About Us</span></nav>
    <nav class="nav right"><span>News</span><span>Testimonials</span><span>Contact</span></nav>
  </header>

  <section class="hero">
    <div class="hero-photo" role="img" aria-label="Dusk photograph of a city skyline"></div>
    <div class="hero-inner">
      <h2>MARCUS T. BELLAMY, LLC</h2>
      <div class="tag">Attorney at Law</div>
      <p>Sed ut perspiciatis unde omnis iste natus error sit voluptatem accusantium.</p>
      <span class="btn">GET A QUOTE</span>
      <div class="pager"><span>←</span><span>1 of 3</span><span>→</span></div>
    </div>
    <svg class="slant" width="494" height="20"><polygon points="0,20 494,0 494,20" fill="#cdb43a"/></svg>
  </section>

  <section class="about">
    <div class="head"><div class="label">ABOUT</div><div class="sec-title">MARCUS T. BELLAMY</div></div>
    <div class="about-copy">
      <h3>26 YEARS OF PRACTICE</h3>
      <p>Sed ut perspiciatis unde omnis iste natus error sit voluptatem accus antium dolore mque laudantium, totam rem aperiam, eaque ipsa quae ab illo inventore veritatis et quasi architecto beatae vitae dicta sunt explicabo. Nemo enim ipsam voltatem quia voluptas sit aspernatur aut odit aut fugit.</p>
      <span class="btn">LEARN MORE</span>
    </div>
    <div class="frame"><div class="pager"><span>←</span><span>1 of 3</span><span>→</span></div></div>
    <div class="video" role="img" aria-label="Video still of the attorney in conversation with a client at a desk"><span class="play"></span></div>
  </section>

  <section class="practice">
    <h2>PRACTICE AREAS</h2>
    <div class="tiles">
      <div class="tile" role="img" aria-label="Courthouse columns">Federal and Capital Cases</div>
      <div class="tile b" role="img" aria-label="Dim interior scene">Serious Felonies</div>
      <div class="tile c" role="img" aria-label="Family meeting with a counselor">Custody Battles</div>
      <div class="tile" role="img" aria-label="Laptop at a legal office">Lorem Ipsum</div>
      <div class="tile c" role="img" aria-label="Signing documents">Lorem Ipsum</div>
      <div class="tile" role="img" aria-label="Colleagues reviewing papers">Lorem Ipsum</div>
    </div>
    <svg class="slant" width="494" height="20"><polygon points="0,2 494,14 494,20 0,20" fill="#2a2a2a"/></svg>
  </section>

  <section class="reviews">
    <div class="head"><div class="label">REVIEWS</div><div class="sec-title">OUR CLIENTS</div></div>
    <div class="quote" style="left:46px"><p>At vero eos et accusamus et iusto odio dignissimos ducimus qui blanditiis prae entium volupt deleniti atque corrupti quos cati cupiditate non provident, sique sunt in culpa qui officia.</p><div class="by">JULIAN <span>/ Oct 25 2021</span></div></div>
    <div class="quote" style="left:261px"><p>At vero eos et accusamus et iusto odio dignissimos ducimus qui blanditiis prae entium volupt deleniti atque corrupti quos cati cupiditate non provident, sique sunt in culpa qui officia.</p><div class="by">JULIAN <span>/ Oct 25 2021</span></div></div>
    <div class="pager"><span>←</span><span>1 of 3</span><span>→</span></div>
    <div class="center-btn" style="top:193px"><span class="btn">VIEW ALL</span></div>
  </section>

  <section class="awards">
    <h2>AWARDS AND MEMBERSHIP</h2>
    <div class="badges">
      <div class="badge" role="img" aria-label="Membership badge"><span class="seal"></span></div>
      <div class="badge" role="img" aria-label="Membership badge"><span class="seal"></span></div>
      <div class="badge" role="img" aria-label="Membership badge"><span class="seal"></span></div>
      <div class="badge" role="img" aria-label="Membership badge"><span class="seal"></span></div>
    </div>
  </section>

  <section class="blog">
    <svg class="slant" style="top:0;bottom:auto" width="494" height="20"><polygon points="0,0 494,0 494,18 0,6" fill="#2a2a2a"/></svg>
    <div class="head"><div class="label">NEWS</div><div class="sec-title">LATEST BLOG</div></div>
    <article class="post" style="left:61px"><h4>Sed ut perspiciatis unde omnis natus error sit volupt</h4><p>Sed ut perspiciatis unde omnis natus error sit volupt Sed ut perspiciati unde omnis natus error.</p><div class="more">READ MORE &nbsp;→</div></article>
    <article class="post" style="left:258px"><h4>Sed ut perspiciatis unde omnis natus error sit volupt</h4><p>Sed ut perspiciatis unde omnis natus error sit volupt Sed ut perspiciati unde omnis natus error.</p><div class="more">READ MORE &nbsp;→</div></article>
    <div class="center-btn" style="top:238px"><span class="btn">VIEW ALL</span></div>
  </section>

  <section class="case">
    <h2>GET YOUR CASE STARTED</h2>
    <div class="form">
      <div class="row"><div class="field">Name</div><div class="field">Email</div><div class="field">Phone</div></div>
      <div class="field msg">Message</div>
    </div>
    <div class="center-btn"><span class="btn ink">SUBMIT NOW</span></div>
  </section>

  <footer class="site-footer">
    <div class="foot-brand"><div class="mark"></div><div class="name">MARCUS T. BELLAMY, LLC</div></div>
    <ul class="contact">
      <li><svg width="7" height="9" viewBox="0 0 10 13"><path d="M5 0a5 5 0 0 1 5 5c0 3.5-5 8-5 8S0 8.5 0 5a5 5 0 0 1 5-5z" fill="#cdb43a"/><circle cx="5" cy="5" r="2" fill="#1c1c1c"/></svg><span>2400 Harbor Crest Avenue<br>suite 300, Ridgeport,<br>Ohio 44102</span></li>
      <li><svg width="7" height="7" viewBox="0 0 10 10"><path d="M2 0l2 2.5-1.2 1.3a6 6 0 0 0 3.4 3.4L7.5 6 10 8l-1.5 2C4 10 0 6 0 1.5z" fill="#cdb43a"/></svg><span>404-555-0172</span></li>
      <li><svg width="8" height="6" viewBox="0 0 10 7"><rect width="10" height="7" fill="#cdb43a"/><path d="M0 0l5 4 5-4" fill="none" stroke="#1c1c1c"/></svg><span>attorneybellamy@<br>mailhub.com</span></li>
    </ul>
    <div class="foot-col nav-col"><h5>Navigation</h5>Home<br>Practice Area<br>About Us<br>News<br>Testimonials<br>Contact</div>
    <div class="foot-col news-col"><h5>Newsletter</h5>At vero eos et accusamus et iusto odio dignissimos ducimus qui<div class="input">Enter email</div><span class="btn">SUBMIT NOW</span></div>
    <div class="foot-rule"></div>
    <div class="copy">2021 Marcus T. Bellamy. All Rights Reserved.</div>
    <div class="social" aria-label="Social profiles"><i></i><i></i></div>
  </footer>
</div>

</body>
</html>
```